Carpentry and Building Business Card

I'm looking for a business card that is minimalistic and that incorporates the theme of my Velmor logo.
On one side I'd like the VELMOR logo with my details on the other side.
Double sided with curved edges

Target Market(s)

Construction / renovation
Adults

Industry/Entity Type

Tradesman

Contact Information for Business Card

Logo on one side, details on the other

Colors

Designer to choose only greyscale colors for use in the design.

Requirements
Must have
• Nilo Petrakis
VELMOR CONSTRUCT
Carpentry & Building Services
0481236574
Velmorconstruct@brixmail.com
Lic No. 718263D
Nice to have
• Fb and insta icons. @velmorconstruct
Should not have
• No hammer or tool icons please.

No address line.

```html
<!DOCTYPE html>
<html lang="en">
<head>
<meta charset="UTF-8">
<title>Velmor Business Card</title>
<link rel="stylesheet" href="https://fonts.googleapis.com/css2?family=Montserrat:wght@500&family=Arimo:wght@400;700&display=swap">
<style>
  :root {
    --backdrop: #2b2b2e;
    --card: #1c1c1d;
    --ink: #f4f4f4;
    --accent: #ee9035;
  }
  * { box-sizing: border-box; margin: 0; padding: 0; }
  html, body {
    width: 1200px;
    height: 948px;
    overflow: hidden;
    background: var(--backdrop);
  }
  .canvas {
    position: relative;
    width: 1200px;
    height: 948px;
  }
  .card {
    position: absolute;
    left: 290px;
    width: 620px;
    height: 354px;
    background: var(--card);
    border-radius: 28px;
    box-shadow: 0 18px 40px rgba(0, 0, 0, 0.45);
    overflow: hidden;
  }
  .card--front { top: 80px; }
  .card--back { top: 514px; }

  .brand {
    position: absolute;
    display: flex;
    align-items: center;
    gap: 22px;
  }
  .brand__mark {
    width: 46px;
    height: 46px;
    border: 2px solid var(--accent);
  }
  .brand__name {
    font-family: "Montserrat", sans-serif;
    font-weight: 500;
    color: var(--ink);
    letter-spacing: 0.32em;
  }
  .card--front .brand {
    left: 50%;
    top: 50%;
    transform: translate(-50%, -50%);
  }
  .card--front .brand__name { font-size: 50px; }

  .card--back .brand {
    left: 52px;
    top: 74px;
    gap: 18px;
  }
  .card--back .brand__mark { width: 38px; height: 38px; }
  .card--back .brand__name { font-size: 38px; }

  .person {
    position: absolute;
    right: 44px;
    top: 150px;
    text-align: right;
    font-family: "Arimo", sans-serif;
  }
  .person__name {
    font-weight: 700;
    font-size: 30px;
    color: var(--accent);
    line-height: 1.05;
  }
  .person__role {
    font-size: 15px;
    color: var(--ink);
    margin-top: 2px;
  }

  .divider {
    position: absolute;
    left: 44px;
    right: 30px;
    top: 222px;
    height: 1.5px;
    background: var(--accent);
  }

  .contact {
    position: absolute;
    left: 58px;
    top: 238px;
    list-style: none;
    font-family: "Arimo", sans-serif;
    font-size: 17px;
    color: var(--ink);
  }
  .contact li {
    display: flex;
    align-items: center;
    gap: 8px;
    height: 27px;
  }
  .contact__icon {
    width: 14px;
    height: 14px;
    flex: none;
  }
  .contact__plain { padding-left: 0; }
</style>
</head>
<body>
<main class="canvas">
  <section class="card card--front" aria-label="Card front">
    <div class="brand">
      <span class="brand__mark"></span>
      <span class="brand__name">VELMOR.</span>
    </div>
  </section>

  <section class="card card--back" aria-label="Card back">
    <div class="brand">
      <span class="brand__mark"></span>
      <span class="brand__name">VELMOR.</span>
    </div>

    <div class="person">
      <p class="person__name">Nilo Petrakis</p>
      <p class="person__role">Carpentry &amp; Building Services</p>
    </div>

    <div class="divider"></div>

    <ul class="contact">
      <li class="contact__plain">Lic No. 718263D</li>
      <li>
        <svg class="contact__icon" viewBox="0 0 24 24" aria-hidden="true">
          <path fill="#ee9035" d="M6.6 10.8a15.1 15.1 0 0 0 6.6 6.6l2.2-2.2a1 1 0 0 1 1-.25 11.4 11.4 0 0 0 3.6.57 1 1 0 0 1 1 1V20a1 1 0 0 1-1 1A17 17 0 0 1 3 4a1 1 0 0 1 1-1h3.5a1 1 0 0 1 1 1c0 1.25.2 2.45.57 3.57a1 1 0 0 1-.25 1z"/>
        </svg>
        0481236574
      </li>
      <li>
        <svg class="contact__icon" viewBox="0 0 24 24" aria-hidden="true">
          <rect x="2" y="5" width="20" height="14" fill="#ee9035"/>
          <path d="M2 5l10 8 10-8" fill="none" stroke="#1c1c1d" stroke-width="2"/>
        </svg>
        Velmorconstruct@brixmail.com
      </li>
    </ul>
  </section>
</main>
</body>
</html>
```